Somebody commencing retirement at age 67 and wanting a card to introduce myself

Something that depicts the activities I intend to pursue in retirement: Travel, Golf (both in Australia and internationally), wining (red) and dining and generally leading a decadent lifestyle with my wife (or by myself as appropriate).

I offer no services, but intend to have a decadent, relaxing
retirement, playing golf, drinking red wine and dining at good
restaurants!

The card needs to have a suitably designed logo that reflects the
foregoing.

Requirements
Must have
• On the front of the card, my photograph (attached and cropped as
• appropriate), my name (Neil Corbishley), my mobile phone number (+61 417
• 382 514), my email address (neil@corbishley.net.au) and my residential
• address (41 Marlowvale Road, Kestrelton, Western Australia 6187,
• Australia).
• The rear of the card should have my postal address (Neil Corbishley
• Post Office Box 418 Brindlecove Western Australia 6951, Australia.)._

```html
<!DOCTYPE html>
<html lang="en">
<head>
<meta charset="utf-8">
<title>Neil Corbishley – Business Card</title>
<link rel="stylesheet" href="https://fonts.googleapis.com/css2?family=Open+Sans:wght@400;600;700&display=swap">
<style>
  :root {
    --page-bg: #2a2c30;
    --card-black: #050507;
    --card-glow: #1b1d3c;
    --blue-1: #0fa3d8;
    --blue-2: #0b86b8;
    --blue-3: #3cc3ee;
    --blue-4: #086c96;
    --grey-1: #f2f2f2;
    --grey-2: #c4c4c4;
    --grey-3: #8e8e8e;
    --grey-4: #5e5e5e;
    --photo-grey: #9a9a9a;
    --text-white: #ffffff;
    --text-soft: #d6d8e4;
  }
  * { box-sizing: border-box; margin: 0; padding: 0; }
  html, body { width: 1200px; height: 900px; overflow: hidden; }
  body {
    background: var(--page-bg);
    font-family: "Open Sans", Arial, sans-serif;
    color: var(--text-white);
    position: relative;
  }
  .card {
    position: absolute;
    border-radius: 22px;
    overflow: hidden;
    background: radial-gradient(ellipse at 45% 55%, var(--card-glow) 0%, #0c0d1c 45%, var(--card-black) 80%);
    box-shadow: 0 18px 40px rgba(0,0,0,0.45);
  }
  .card svg.blocks { position: absolute; display: block; }

  /* Back (portrait) */
  .card--back { left: 140px; top: 170px; width: 320px; height: 560px; }
  .card--back .blocks--top { top: 0; right: 0; }
  .card--back .blocks--bottom { bottom: 0; right: 0; }
  .logo-placeholder {
    position: absolute;
    top: 112px; left: 152px;
    writing-mode: vertical-rl;
    font-size: 54px; font-weight: 600;
    letter-spacing: 1px; line-height: 1;
  }
  .leisure-icons {
    position: absolute; left: 30px; top: 130px;
    display: flex; flex-direction: column; gap: 16px;
  }
  .leisure-icons svg { display: block; }
  .postal-address {
    position: absolute; left: 30px; top: 272px;
    font-size: 10px; line-height: 1.45;
    font-style: normal; color: var(--text-soft);
  }
  .postal-address strong { font-weight: 700; color: var(--text-white); }

  /* Front (landscape) */
  .card--front { left: 500px; top: 290px; width: 560px; height: 320px; }
  .card--front .blocks--top { top: 0; left: 300px; }
  .card--front .blocks--bottom { bottom: 0; right: 0; }
  .portrait {
    position: absolute; left: 150px; top: 30px;
    width: 140px; height: 140px; border-radius: 50%;
    background: radial-gradient(circle at 50% 40%, #b4b4b4, var(--photo-grey));
    border: 5px solid #f5f5f5;
    box-shadow: 0 0 0 3px var(--blue-1);
  }
  .holder-name {
    position: absolute; left: 40px; top: 196px;
    font-size: 24px; font-weight: 700; letter-spacing: 0.5px;
    text-transform: uppercase;
  }
  .contact-list { position: absolute; left: 326px; top: 66px; list-style: none; }
  .contact-list li {
    display: flex; align-items: flex-start; gap: 12px;
    font-size: 13px; line-height: 1.2; margin-bottom: 10px;
  }
  .contact-list .icon {
    flex: none; width: 26px; height: 26px; border-radius: 50%;
    background: var(--blue-1);
    display: flex; align-items: center; justify-content: center;
  }
  .contact-list .label { padding-top: 4px; }
</style>
</head>
<body>

<!-- Back of card -->
<section class="card card--back" aria-label="Card back">
  <svg class="blocks blocks--top" width="200" height="90" viewBox="0 0 200 90" aria-hidden="true">
    <rect x="0" y="0" width="40" height="30" fill="var(--grey-2)"/>
    <rect x="40" y="0" width="40" height="30" fill="var(--grey-1)"/>
    <rect x="80" y="0" width="40" height="30" fill="var(--grey-2)"/>
    <rect x="120" y="0" width="40" height="30" fill="var(--grey-3)"/>
    <rect x="160" y="0" width="40" height="30" fill="var(--grey-2)"/>
    <rect x="40" y="30" width="40" height="30" fill="var(--grey-3)"/>
    <rect x="80" y="30" width="40" height="30" fill="var(--grey-1)"/>
    <rect x="160" y="30" width="40" height="30" fill="var(--grey-3)"/>
    <rect x="80" y="60" width="40" height="30" fill="var(--grey-4)"/>
  </svg>
  <svg class="blocks blocks--bottom" width="220" height="120" viewBox="0 0 220 120" aria-hidden="true">
    <rect x="0" y="0" width="40" height="40" fill="var(--grey-3)"/>
    <rect x="180" y="0" width="40" height="40" fill="var(--grey-2)"/>
    <rect x="0" y="40" width="40" height="40" fill="var(--grey-2)"/>
    <rect x="40" y="40" width="40" height="40" fill="var(--grey-3)"/>
    <rect x="140" y="40" width="40" height="40" fill="var(--grey-2)"/>
    <rect x="180" y="40" width="40" height="40" fill="var(--grey-1)"/>
    <rect x="0" y="80" width="40" height="40" fill="var(--grey-1)"/>
    <rect x="40" y="80" width="40" height="40" fill="var(--grey-2)"/>
    <rect x="80" y="80" width="40" height="40" fill="var(--grey-1)"/>
    <rect x="120" y="80" width="40" height="40" fill="var(--grey-1)"/>
    <rect x="160" y="80" width="60" height="40" fill="var(--grey-2)"/>
  </svg>

  <div class="leisure-icons" aria-label="Wine, dining and travel">
    <svg width="30" height="30" viewBox="0 0 30 30" aria-hidden="true">
      <path d="M9 4h12l-1 8a5 5 0 0 1-10 0z" fill="#fff"/>
      <rect x="14" y="16" width="2" height="8" fill="#fff"/>
      <rect x="9" y="24" width="12" height="2" fill="#fff"/>
    </svg>
    <svg width="30" height="30" viewBox="0 0 30 30" aria-hidden="true">
      <circle cx="15" cy="15" r="13" fill="none" stroke="#fff" stroke-width="2.5"/>
      <circle cx="15" cy="15" r="8" fill="#fff"/>
      <rect x="11" y="9" width="2" height="12" fill="#000"/>
      <rect x="17" y="9" width="2" height="12" fill="#000"/>
    </svg>
    <svg width="30" height="30" viewBox="0 0 30 30" aria-hidden="true">
      <path d="M15 2l2 9 10 5v3l-10-3-1 7 3 2v2l-4-1-4 1v-2l3-2-1-7-10 3v-3l10-5z" fill="#fff"/>
    </svg>
  </div>

  <address class="postal-address">
    <strong>Neil Corbishley</strong><br>
    Post Office Box 418<br>
    Brindlecove<br>
    Western Australia<br>
    6951, Australia
  </address>

  <div class="logo-placeholder">LOGO HERE</div>
</section>

<!-- Front of card -->
<section class="card card--front" aria-label="Card front">
  <svg class="blocks blocks--top" width="180" height="80" viewBox="0 0 180 80" aria-hidden="true">
    <rect x="0" y="0" width="30" height="20" fill="var(--blue-2)"/>
    <rect x="30" y="0" width="30" height="20" fill="var(--blue-1)"/>
    <rect x="60" y="0" width="30" height="20" fill="var(--blue-3)"/>
    <rect x="90" y="0" width="30" height="20" fill="var(--blue-1)"/>
    <rect x="120" y="0" width="30" height="20" fill="var(--blue-2)"/>
    <rect x="150" y="0" width="30" height="20" fill="var(--blue-1)"/>
    <rect x="30" y="20" width="30" height="20" fill="var(--blue-4)"/>
    <rect x="60" y="20" width="30" height="20" fill="var(--blue-1)"/>
    <rect x="120" y="20" width="30" height="20" fill="var(--blue-4)"/>
    <rect x="150" y="20" width="30" height="20" fill="var(--blue-2)"/>
    <rect x="60" y="40" width="30" height="20" fill="var(--blue-4)"/>
  </svg>
  <svg class="blocks blocks--bottom" width="167" height="100" viewBox="0 0 200 120" aria-hidden="true">
    <rect x="0" y="0" width="40" height="40" fill="var(--blue-2)"/>
    <rect x="160" y="0" width="40" height="40" fill="var(--blue-1)"/>
    <rect x="0" y="40" width="40" height="40" fill="var(--blue-1)"/>
    <rect x="40" y="40" width="40" height="40" fill="var(--blue-2)"/>
    <rect x="120" y="40" width="40" height="40" fill="var(--blue-1)"/>
    <rect x="160" y="40" width="40" height="40" fill="var(--blue-3)"/>
    <rect x="0" y="80" width="40" height="40" fill="var(--blue-3)"/>
    <rect x="40" y="80" width="40" height="40" fill="var(--blue-1)"/>
    <rect x="80" y="80" width="40" height="40" fill="var(--blue-3)"/>
    <rect x="120" y="80" width="40" height="40" fill="var(--blue-3)"/>
    <rect x="160" y="80" width="40" height="40" fill="var(--blue-1)"/>
  </svg>

  <div class="portrait" role="img" aria-label="Portrait photograph of Neil Corbishley"></div>
  <h1 class="holder-name">Neil Corbishley</h1>

  <ul class="contact-list">
    <li>
      <span class="icon"><svg width="14" height="14" viewBox="0 0 14 14" aria-hidden="true"><path d="M3 1l2 3-1.3 1.3a8 8 0 0 0 5 5L10 9l3 2-1 2c-6 0-11-5-11-11z" fill="#fff"/></svg></span>
      <span class="label">+61 417 382 514</span>
    </li>
    <li>
      <span class="icon"><svg width="14" height="14" viewBox="0 0 14 14" aria-hidden="true"><path d="M1 6l12-5-4 12-2-5z" fill="#fff"/></svg></span>
      <span class="label">neil@corbishley.net.au</span>
    </li>
    <li>
      <span class="icon"><svg width="14" height="14" viewBox="0 0 14 14" aria-hidden="true"><path d="M7 1a4 4 0 0 1 4 4c0 3-4 8-4 8S3 8 3 5a4 4 0 0 1 4-4z" fill="#fff"/><circle cx="7" cy="5" r="1.5" fill="var(--blue-1)"/></svg></span>
      <span class="label">41 Marlowvale Road,<br>Kestrelton<br>Western Australia 6187<br>Australia</span>
    </li>
  </ul>
</section>

</body>
</html>
```